We need a business card design for our website qvwtrading.net. The Star Headline is qvwtrading.net, in large lettering.We sell fashion rings of titanium, mirror pollished stainless steel, and related jewelry. Basically quality products competing with the high expense of gold.We have to portray honesty and trust, because thats who I am. I know marketing, but I am weak on colors and layout. 3D Gold curved edge letters are ok. No green and yellow.Black,Red,Purple and White in small amounts.No fancy Lettering.
No Rainbows in printing.
Our goal is selling our products online globally

Kind Regards Maren Tulloch

Fashion

qvwtrading.net
known for our ideal fit rings
email.marentullochptyltd@corvexmail com

```html
<!DOCTYPE html>
<html lang="en">
<head>
<meta charset="utf-8">
<title>qvwtrading.net business card</title>
<link href="https://fonts.googleapis.com/css2?family=Cormorant+Garamond:ital,wght@1,300&family=Ubuntu:wght@300;400&display=swap" rel="stylesheet">
<style>
  :root {
    --backdrop: #e8e8e8;
    --card-top: #5f5f5f;
    --card-bottom: #1c1c1c;
    --contact-ink: #ffffff;
    --headline-ink: #d6d6d6;
    --tagline-ink: #c4c4c4;
    --card-shadow: rgba(0, 0, 0, 0.28);
  }
  html, body {
    margin: 0;
    padding: 0;
    overflow: hidden;
  }
  .stage {
    position: relative;
    width: 1200px;
    height: 720px;
    background: var(--backdrop);
    overflow: hidden;
  }
  .card {
    position: absolute;
    top: 215px;
    width: 520px;
    height: 290px;
    border-radius: 3px;
    background: linear-gradient(160deg, var(--card-top) 0%, var(--card-bottom) 100%);
    box-shadow: 0 10px 24px var(--card-shadow);
    box-sizing: border-box;
  }
  .card--contact { left: 50px; }
  .card--headline { left: 630px; }

  .contact-list {
    position: absolute;
    left: 36px;
    bottom: 40px;
    margin: 0;
    padding: 0;
    list-style: none;
    font-family: "Ubuntu", sans-serif;
    font-weight: 400;
    font-size: 18px;
    line-height: 1.75;
    color: var(--contact-ink);
    letter-spacing: 0.2px;
  }

  .headline-block {
    position: absolute;
    left: 170px;
    top: 100px;
  }
  .headline {
    margin: 0;
    font-family: "Cormorant Garamond", serif;
    font-style: italic;
    font-weight: 300;
    font-size: 56px;
    line-height: 1;
    color: var(--headline-ink);
  }
  .tagline {
    margin: 14px 0 0 4px;
    font-family: "Ubuntu", sans-serif;
    font-weight: 300;
    font-size: 18px;
    color: var(--tagline-ink);
    letter-spacing: 0.3px;
  }
</style>
</head>
<body>
  <main class="stage">
    <section class="card card--contact" aria-label="Card back with contact details">
      <ul class="contact-list">
        <li class="contact-web">www.qvwtrading.net</li>
        <li class="contact-email">marentullochptyltd@corvexmail com</li>
      </ul>
    </section>

    <section class="card card--headline" aria-label="Card front with headline">
      <div class="headline-block">
        <h1 class="headline">qvwtrading.net</h1>
        <p class="tagline">known for our ideal fit rings</p>
      </div>
    </section>
  </main>
</body>
</html>
```